Naturopath specialising in Children's Health

I have just started working in a new clinic where I will be predominantly treating children so I would like to rebrand with a business card that reflects this.

I would like a clever design which is subtly playful and will attract children and parents alike, while maintaining a professional look. It must also reflect that I utilize natural medicine - including herbal medicine and nutrition as part of my treatment. Employing the use of a plant or herb would be ideal. I had envisioned the image of a dandelion blowing in the wind (or being blown by a child) as a great combination of the playful yet natural medicine I am trying to ecompass in the card.

I would like to use yellow, orange, blue or green as the dominant colour for the card.

The front of the card should contain the logo and the words 'Maribel Stroud - Naturopath.'

The back of the card should contain the following details:
Maribel Stroud BHSc Nat, Dip RM
Naturopath, Herbalist, Nutritionist, Iridologist, Remedial Massage Therapist, Reiki Practitioner
0413 927 186
Willowfern Haven - (02) 9731 4068
maribel.stroud@kestrelmail.example
NHPA 81347

Industry/Entity Type

Clinic

```html
<!DOCTYPE html>
<html lang="en">
<head>
<meta charset="utf-8">
<title>Maribel Stroud – Naturopath business card</title>
<link href="https://fonts.googleapis.com/css2?family=Quicksand:wght@400&family=Nunito:wght@700;800&family=Open+Sans:wght@400;600&display=swap" rel="stylesheet">
<style>
  :root {
    --page: #ece8e1;
    --card: #ffffff;
    --card-edge: #e6e6e6;
    --leaf: #8cc63f;
    --leaf-light: #c3e28c;
    --leaf-deep: #5fa227;
    --sun: #f5a91e;
    --sun-soft: #fbd48a;
    --ink: #4a4a4a;
    --icon: #f07d1a;
  }
  * { box-sizing: border-box; margin: 0; padding: 0; }
  html, body { width: 1200px; height: 1023px; overflow: hidden; }
  body {
    background: var(--page);
    display: flex; flex-direction: column; align-items: center; justify-content: center;
    gap: 40px;
  }
  .card {
    position: relative;
    width: 820px; height: 468px;
    background: linear-gradient(135deg, #ffffff 0%, #f4f4f4 100%);
    border-radius: 22px;
    border: 1px solid var(--card-edge);
    box-shadow: 0 8px 22px rgba(0,0,0,.14);
    overflow: hidden;
  }

  /* Front */
  .front-hills {
    position: absolute; left: 0; bottom: 0; width: 100%; height: 170px;
  }
  .dandelion-art {
    position: absolute; left: 150px; top: 110px; width: 200px; height: 170px;
    border-radius: 50%;
    background: radial-gradient(circle, var(--sun-soft) 0%, rgba(251,212,138,.35) 55%, rgba(255,255,255,0) 72%);
  }
  .front-title {
    position: absolute; left: 330px; top: 130px;
  }
  .front-name {
    font-family: "Quicksand", sans-serif; font-weight: 400;
    font-size: 66px; color: var(--leaf); line-height: 1;
  }
  .front-role {
    font-family: "Nunito", sans-serif; font-weight: 800;
    font-size: 56px; color: var(--sun); line-height: 1.05;
    margin-left: 112px;
  }

  /* Back */
  .back-seeds {
    position: absolute; inset: 0;
    background: radial-gradient(ellipse at 70% 75%, rgba(251,212,138,.22) 0%, rgba(255,255,255,0) 60%);
  }
  .back-details { position: absolute; left: 46px; top: 40px; font-family: "Open Sans", sans-serif; color: var(--ink); }
  .back-name {
    font-family: "Nunito", sans-serif; font-weight: 800;
    font-size: 38px; color: var(--sun); letter-spacing: .5px; text-transform: uppercase;
  }
  .back-name .credentials { font-weight: 700; font-size: 25px; color: var(--leaf); text-transform: none; letter-spacing: 0; margin-left: 6px; }
  .back-roles { font-size: 19px; line-height: 1.4; margin-top: 4px; }
  .contact-list { list-style: none; margin-top: 8px; font-size: 19px; line-height: 1.45; }
  .contact-list li { display: flex; align-items: center; gap: 9px; }
  .contact-icon { width: 20px; height: 20px; flex: none; }
  .contact-note { color: var(--leaf); }
  .registration { margin-left: 0; }
</style>
</head>
<body>

<section class="card card-front" aria-label="Card front">
  <div class="dandelion-art" role="img" aria-label="Dandelion seed head illustration in soft orange"></div>
  <svg class="front-hills" viewBox="0 0 820 170" preserveAspectRatio="none" role="img" aria-label="Green illustration of a child blowing a dandelion">
    <defs>
      <linearGradient id="hillFill" x1="0" y1="0" x2="1" y2="0">
        <stop offset="0" stop-color="#6fb22f"/>
        <stop offset="1" stop-color="#c3e28c"/>
      </linearGradient>
    </defs>
    <path d="M0 40 C120 10 260 20 380 0 C460 40 520 110 600 130 C680 150 760 120 820 110 L820 170 L0 170 Z" fill="url(#hillFill)"/>
  </svg>
  <div class="front-title">
    <p class="front-name">Maribel Stroud</p>
    <p class="front-role">Naturopath</p>
  </div>
</section>

<section class="card card-back" aria-label="Card back">
  <div class="back-seeds" role="img" aria-label="Scattered dandelion seeds drifting across the card"></div>
  <div class="back-details">
    <h1 class="back-name">Maribel Stroud<span class="credentials">BHSc Nat, Dip RM</span></h1>
    <p class="back-roles">Naturopath, Herbalist, Nutritionist<br>Iridologist, Remedial Massage Therapist, Reiki Practitioner</p>
    <ul class="contact-list">
      <li>
        <svg class="contact-icon" viewBox="0 0 20 20" aria-hidden="true"><circle cx="10" cy="10" r="10" fill="var(--icon)"/><path d="M7 5.5 L8.6 5.5 L9.3 8 L8.2 8.9 C8.8 10.3 9.7 11.2 11.1 11.8 L12 10.7 L14.5 11.4 L14.5 13 C14.5 13.6 14 14 13.4 14 C9.4 13.7 6.3 10.6 6 6.6 C6 6 6.4 5.5 7 5.5 Z" fill="#fff"/></svg>
        <span>0413 927 186</span>
      </li>
      <li>
        <svg class="contact-icon" viewBox="0 0 20 20" aria-hidden="true"><circle cx="10" cy="10" r="10" fill="var(--icon)"/><path d="M7 5.5 L8.6 5.5 L9.3 8 L8.2 8.9 C8.8 10.3 9.7 11.2 11.1 11.8 L12 10.7 L14.5 11.4 L14.5 13 C14.5 13.6 14 14 13.4 14 C9.4 13.7 6.3 10.6 6 6.6 C6 6 6.4 5.5 7 5.5 Z" fill="#fff"/></svg>
        <span>(02) 9731 4068 <span class="contact-note">[Willowfern Haven]</span></span>
      </li>
      <li>
        <svg class="contact-icon" viewBox="0 0 20 20" aria-hidden="true"><circle cx="10" cy="10" r="10" fill="var(--icon)"/><rect x="5" y="6.5" width="10" height="7" rx="1" fill="#fff"/><path d="M5.5 7 L10 10.5 L14.5 7" fill="none" stroke="var(--icon)" stroke-width="1.2"/></svg>
        <span>maribel.stroud@kestrelmail.example</span>
      </li>
      <li class="registration"><span>NHPA 81347</span></li>
    </ul>
  </div>
</section>

</body>
</html>
```